Webdesign für eine Softwarewarentwicklung und Consulting für das Gesundheitswesen
Zielgruppe
Softwarewarentwicklung und Consulting für das Gesundheitswesen. Unsere Zielgruppe sind Unternehmen und Organisationen im Bereich des Gesundheitswesen. Weiter informationen auf derzeitiger Homepage unter www.vmt-pflegeloesung.de.
Aufgabenstellung
Das Webdesign sollte deutlich moderner und kreativer wirken als unsere derzeitige Hompage. (Die bisherige Hompage wurde seinerzeit bei der Gründung 'auf die Schnelle' entwickelt.) Die neue Homapage sollte 'frisch' wirken und einem modernen Softwareunternehmen entsprechen.: Schlicht, modern und innovativ. Die Website sollte auch später gut auf Handy und Tablet darstellbar sein. Da wir derzeit wenig Inhalte auf unserer Homepage haben, wären wir auch für inhaltliche Vorschläge dankbar. Unsere Logofarben sollten sich auch im Design wiederfinden (der Rotton hat den Wert RGB: 227, 7, 19 #e30713 - der Blauton hat den Wert RGB: 30, 38, 74 1 #e264a).
Im Format bin ich unerfahren und würde dann für das spätere Umsetzen Adobe Photoshop vorschlagen.
Idealerweise sollte sich das Design später in einem gängigen CMS umsetzen lassen.
Gerne können Sie uns auch ein Komplettangebot auch zum Thema Umsetzung unterbreiten.
Grundsätzlich finde ich folgende Hompages ganz gut:
https://brelvuno.com/
https://www.kiesfeld.de/
https://www.plumvantic.com/de/
https://zirkanu.de/

```html
<!DOCTYPE html>
<html lang="de">
<head>
<meta charset="utf-8">
<title>VMT – Softwareentwicklung für das Gesundheitswesen</title>
<link rel="stylesheet" href="https://fonts.googleapis.com/css2?family=Lato:ital,wght@0,300;0,400;0,700;0,900;1,400&display=swap">
<style>
:root{
  --red:#e30713;
  --navy:#1e264a;
  --navy-2:#2c3666;
  --text:#2a2a2a;
  --muted:#444;
  --light:#f4f5f8;
  --white:#fff;
}
*{box-sizing:border-box;margin:0;padding:0}
html,body{width:1200px;height:2629px;overflow:hidden}
body{font-family:"Lato",sans-serif;color:var(--text);background:var(--white);position:relative}
.wrap{position:relative;width:900px;margin:0 auto}
a{color:inherit;text-decoration:none}

/* header */
.site-header{height:58px;border-top:3px solid var(--navy);border-bottom:1px dashed #bbb;position:relative}
.brand{position:absolute;left:0;top:8px;display:flex;align-items:center;gap:6px;font-weight:900;font-size:34px;color:var(--red);letter-spacing:2px}
.brand-dot{width:10px;height:10px;background:var(--navy)}
.nav{position:absolute;right:0;top:11px;display:flex;align-items:center;font-size:12px;font-weight:700;color:var(--navy)}
.nav a{padding:0 18px;line-height:30px;position:relative}
.nav a.active::after{content:"";position:absolute;left:0;right:0;top:41px;height:3px;background:var(--red)}
.nav a.cta{background:var(--red);color:#fff;border-radius:16px;padding:0 20px}

/* hero */
.hero{height:457px;position:relative;text-align:center;border-bottom:1px dashed #bbb}
.hero-photo{position:absolute;inset:0;background:linear-gradient(100deg,#5fb3c4 0%,#a9d6da 20%,#e9eeee 45%,#f3f1ee 60%,#e2c7a3 80%,#c9a985 100%);opacity:.9}
.hero-veil{position:absolute;inset:0;background:radial-gradient(ellipse at 50% 50%,rgba(255,255,255,.85) 0%,rgba(255,255,255,.55) 45%,rgba(255,255,255,0) 75%)}
.hero-inner{position:relative;padding-top:134px}
.hero h1{font-size:42px;font-weight:900;color:var(--navy);line-height:42px}
.hero h1 .thin{font-weight:300}
.hero h1 .red{color:var(--red)}
.hero .lead{font-size:15.5px;font-weight:700;color:var(--navy);margin-top:18px;line-height:19px}
.hero .call{font-size:15px;font-weight:700;color:var(--navy);margin-top:42px}
.hero .phone{font-size:20px;color:var(--navy);margin-top:6px;display:inline-flex;align-items:center;gap:14px;position:relative;padding-bottom:8px}
.hero .phone::after{content:"";position:absolute;right:30px;bottom:0;width:110px;height:3px;border-radius:2px;background:var(--red)}

/* about */
.about{height:373px;position:relative}
.ghost{font-size:54px;font-weight:300;color:#dedede;letter-spacing:1px;line-height:54px}
.about .ghost{position:absolute;left:0;top:44px}
.bar{display:block;width:40px;height:3px;background:var(--red)}
.about .bar{position:absolute;left:0;top:70px}
.sec-title{font-size:24px;font-weight:700;color:var(--navy)}
.sec-title .red{color:var(--red)}
.about .sec-title{position:absolute;left:0;top:79px}
.col{position:absolute;width:424px;font-size:13.2px;line-height:19px;text-align:justify;color:var(--muted)}
.col p+p{margin-top:19px}
.btn{display:inline-block;background:var(--red);color:#fff;font-size:12.5px;font-weight:700;border-radius:16px;width:97px;height:32px;line-height:32px;text-align:center}
.about .btn{position:absolute;left:2px;top:287px}

/* products */
.products{height:700px;background:var(--navy);color:#fff;position:relative;text-align:center}
.products .ghost{color:#fff;font-size:52px;position:absolute;top:42px;width:100%}
.products .sec-title{color:#fff;position:absolute;top:96px;width:100%}
.products .bar{position:absolute;left:430px;top:130px}
.products .intro{position:absolute;top:160px;left:-10px;width:920px;font-size:13.2px;line-height:19px}
.features{position:absolute;top:265px;left:0;width:900px;height:380px}
.feature{position:absolute;width:170px;text-align:center;font-size:17px;font-weight:700}
.feature svg{display:block;margin:0 auto 8px}
.screen{position:absolute;left:240px;top:0;width:422px;height:305px;background:linear-gradient(180deg,#c9ccd4,#9ea3ad);border-radius:12px;padding:16px 16px 56px}
.screen-ui{width:100%;height:100%;background:linear-gradient(180deg,#f0f2f6,#dfe3ea);border-radius:2px;position:relative}
.screen-ui::before{content:"";position:absolute;left:0;top:0;bottom:0;width:56px;background:var(--navy-2)}
.stand{position:absolute;left:397px;top:305px;width:108px;height:38px;background:linear-gradient(180deg,#bfc3cb,#e8eaee);clip-path:polygon(12% 0,88% 0,100% 100%,0 100%)}
.links{position:absolute;top:32px}

/* jobs */
.jobs{height:689px;position:relative}
.jobs .ghost{position:absolute;left:0;top:28px}
.jobs .bar{position:absolute;left:0;top:90px}
.jobs .sec-title{position:absolute;left:0;top:99px}
.jobs h4{font-size:13.5px;font-weight:700;color:var(--navy)}
.team-line{position:absolute;left:2px;top:146px}
.perks{position:absolute;left:2px;top:182px}
.perks li{list-style:none;font-size:13.5px;line-height:23px;color:var(--navy);display:flex;align-items:center;gap:10px}
.job-card{position:absolute;left:663px;top:57px;width:237px;height:202px;background:#fff;box-shadow:0 2px 12px rgba(0,0,0,.12);text-align:center}
.tag{position:absolute;left:-8px;top:12px;background:var(--red);color:#fff;font-size:10px;font-weight:700;padding:2px 16px;clip-path:polygon(0 0,100% 0,92% 100%,0 100%)}
.job-card .role{font-size:13.5px;font-weight:700;color:var(--navy);margin-top:16px}
.job-card .desc{font-size:13px;color:var(--navy);margin-top:14px;line-height:19px}
.question{position:absolute;left:0;top:310px}
.skills{position:absolute;top:364px;left:2px;width:900px}
.skill{position:absolute;font-size:13.2px;color:var(--navy);line-height:19px}
.skill h4{margin-bottom:20px}
.skill ul{list-style:none}
.skill li{padding-left:14px;position:relative}
.skill li::before{content:"›";position:absolute;left:0;top:-1px}
.skill li.plain::before{content:none}
.skill li.plain{padding-left:0}
.apply{position:absolute;left:116px;top:570px;width:662px;height:100px;background:var(--navy);display:flex;color:#fff}
.apply-left{width:332px;padding:22px 20px 0 30px;font-size:14px;font-weight:700;line-height:19px}
.apply-right{flex:1;background:var(--navy-2);padding:14px 0 0 48px;clip-path:polygon(0 0,100% 0,100% 100%,0 100%,22px 50%)}
.apply-right .lbl{font-size:13.5px;font-weight:700}
.contact{display:flex;align-items:center;gap:12px;margin-top:12px;font-size:13.5px;line-height:19px}
.contact b{font-weight:700}

/* testimonials */
.quotes{height:256px;position:relative;background:var(--navy);overflow:hidden}
.quotes .red-half{position:absolute;left:0;top:0;width:700px;height:256px;background:var(--red);clip-path:polygon(0 0,548px 0,700px 256px,0 256px)}
.quote{position:absolute;top:30px;width:372px;color:#fff}
.avatar{width:50px;height:50px;border:2px solid #fff;border-radius:50%}
.quote .text{font-style:italic;font-size:14.3px;line-height:19px;margin-top:16px;text-align:justify}
.quote .who{font-style:normal;font-weight:700;font-size:14px;margin-top:29px}
.qmark{position:absolute;left:566px;top:10px;font-size:130px;font-weight:900;color:rgba(255,255,255,.15);line-height:130px}

/* footer */
.site-footer{height:96px;background:var(--light);position:relative}
.site-footer .brand{top:26px;font-size:32px}
.f-item{position:absolute;display:flex;align-items:center;gap:10px;font-size:11.5px;color:var(--navy)}
.legal{position:absolute;right:0;top:38px;font-size:11.5px;font-weight:700;color:var(--navy)}
</style>
</head>
<body>

<header class="site-header">
  <div class="wrap">
    <a class="brand" href="#"><span class="brand-dot"></span>VMT</a>
    <nav class="nav">
      <a class="active" href="#">HOME</a>
      <a href="#">PRODUKTE</a>
      <a href="#">ÜBER UNS</a>
      <a href="#">JOBANGEBOTE</a>
      <a class="cta" href="#">KONTAKT</a>
    </nav>
  </div>
</header>

<section class="hero">
  <div class="hero-photo" role="img" aria-label="Unscharfes Foto eines hellen Wartebereichs mit türkisen Sitzen und Empfangstresen"></div>
  <div class="hero-veil"></div>
  <div class="hero-inner">
    <h1>Softwareentwicklung <span class="thin">für das</span><br><span class="red">Gesundheitswesen</span></h1>
    <p class="lead">Herr Kwenrich verfügt über 30 Jahre Erfahrung in den Bereichen Softwareentwicklung,<br>Projektsteuerung und Prozessoptimierung im Umfeld eHealth und Abrechnung.</p>
    <p class="call">Rufen Sie jetzt für eine kostenlose Beratung an</p>
    <p class="phone">
      <svg width="22" height="22" viewBox="0 0 24 24" fill="none" stroke="#1e264a" stroke-width="1.6"><path d="M5 3h4l2 5-2.5 1.5a11 11 0 0 0 6 6L16 13l5 2v4a2 2 0 0 1-2 2A17 17 0 0 1 3 5a2 2 0 0 1 2-2z"/></svg>
      +49 30 55 / 1 20 48 -00
    </p>
  </div>
</section>

<section class="about">
  <div class="wrap" style="height:373px">
    <div class="ghost">ÜBER UNS</div>
    <span class="bar"></span>
    <h2 class="sec-title"><span class="red">Erfahrung im</span> Gesundheitswesen</h2>
    <div class="col" style="left:2px;top:125px">
      <p>2019 startete der Gründer Jonas Reimer mit einem erfahrenen Team aus Softwareentwicklern und Beratern aus den Bereichen der IT, Produktion und Onlineanwendung. Seit dem bietet die VMT eine fast einzigartige Fachkompetenz mit jahrzehntelanger Erfahrung im Gesundheitswesen. Jonas Reimer selbst ist mit seinen über 20 Jahren Berufserfahrung erfolgreich im Gesundheitswesen und Apothekenmarkt tätig.</p>
    </div>
    <div class="col" style="left:480px;top:125px">
      <p>Zum 1. Januar 2021 konnte Tobias Kwenrich als weiterer Geschäftsführer für die VMT gewonnen werden.</p>
      <p>Herr Kwenrich verfügt über 30 Jahre Erfahrung in den Bereichen Softwareentwicklung, Projektsteuerung und Prozessoptimierung im Umfeld eHealth und Abrechnung. Seine Expertise wird auch in Zukunft zur weiteren Geschäftsentwicklung der VMT beitragen.</p>
    </div>
    <a class="btn" href="#">Mehr...</a>
  </div>
</section>

<section class="products">
  <div class="wrap" style="height:700px">
    <div class="ghost">PRODUKTE</div>
    <h2 class="sec-title"><span class="red">Digitale</span> Zukunftslösungen</h2>
    <span class="bar"></span>
    <div class="intro">
      <p>Mit höchster Fachkompetenz im IT-Bereich, ist es unser Ziel, Ihr Unternehmen erfolgreich im digitalen Wandel des Gesundheitswesens zu positionieren. Wir entwickeln Strategien und Softwarelösungen, die genau auf Ihr Unternehmen zugeschnitten sind.</p>
      <p style="margin-top:18px">Mit unserem Know-how und der jahrelangen Markterfahrung bieten wir flexible Lösungen in den Bereichen:</p>
    </div>

    <div class="features">
      <svg class="links" style="left:158px" width="46" height="260" viewBox="0 0 46 260" fill="none" stroke="#6a7193" stroke-width="1.2"><path d="M0 0H45V260H0M0 122H45"/><circle cx="3" cy="0" r="2" fill="#6a7193"/><circle cx="3" cy="122" r="2" fill="#6a7193"/><circle cx="3" cy="260" r="2" fill="#6a7193"/></svg>
      <svg class="links" style="left:700px" width="46" height="260" viewBox="0 0 46 260" fill="none" stroke="#6a7193" stroke-width="1.2"><path d="M46 0H1V260H46M46 122H1"/><circle cx="43" cy="0" r="2" fill="#6a7193"/><circle cx="43" cy="122" r="2" fill="#6a7193"/><circle cx="43" cy="260" r="2" fill="#6a7193"/></svg>

      <div class="screen" role="img" aria-label="Bildschirm mit einer Dashboard-Oberfläche der Software"><div class="screen-ui"></div></div>
      <div class="stand"></div>

      <div class="feature" style="left:-14px;top:8px">
        <svg width="50" height="50" viewBox="0 0 50 50" fill="none" stroke="#fff" stroke-width="1.6"><circle cx="25" cy="25" r="9"/><circle cx="25" cy="25" r="3"/><path d="M25 6v6M25 38v6M6 25h6M38 25h6M12 12l4 4M34 34l4 4M38 12l-4 4M12 38l4-4"/></svg>
        Prozessoptimierung
      </div>
      <div class="feature" style="left:-14px;top:136px">
        <svg width="50" height="50" viewBox="0 0 50 50" fill="none" stroke="#fff" stroke-width="1.6"><circle cx="25" cy="25" r="12"/><path d="M13 25h24M25 13c-6 6-6 18 0 24M25 13c6 6 6 18 0 24M4 8h8M38 8h8M4 42h8M38 42h8"/></svg>
        Digitalisierung
      </div>
      <div class="feature" style="left:-14px;top:262px">
        <svg width="50" height="46" viewBox="0 0 50 46" fill="none" stroke="#fff" stroke-width="1.6"><rect x="3" y="4" width="44" height="36" rx="2"/><path d="M3 13h44"/><circle cx="8" cy="8.5" r="1"/><circle cx="12" cy="8.5" r="1"/><circle cx="16" cy="8.5" r="1"/><path d="M28 24l10 4-4 2 4 4-2 2-4-4-2 4z"/></svg>
        Onlineanwendung
      </div>
      <div class="feature" style="left:726px;top:0">
        <svg width="60" height="58" viewBox="0 0 60 58" fill="none" stroke="#fff" stroke-width="2"><rect x="4" y="8" width="22" height="44" rx="11" transform="rotate(-20 15 30)"/><circle cx="42" cy="32" r="15"/><path d="M32 42l20-20"/></svg>
        Rezept / EHealth
      </div>
      <div class="feature" style="left:726px;top:132px">
        <svg width="60" height="54" viewBox="0 0 60 54" fill="none" stroke="#fff" stroke-width="1.8"><rect x="10" y="12" width="40" height="30" rx="6"/><path d="M14 12c0-14 32-14 32 0M22 42l-6 8v-8"/><circle cx="24" cy="27" r="1.3"/><circle cx="30" cy="27" r="1.3"/><circle cx="36" cy="27" r="1.3"/></svg>
        Consulting
      </div>
      <div class="feature" style="left:732px;top:252px">
        <svg width="60" height="60" viewBox="0 0 60 60" fill="none" stroke="#fff" stroke-width="1.6"><rect x="14" y="6" width="36" height="50"/><path d="M22 16h22M22 24h22M22 32h22M22 40h22M8 10v44"/><rect x="26" y="2" width="12" height="6"/></svg>
        Projektmanagement
      </div>
    </div>
  </div>
</section>

<section class="jobs">
  <div class="wrap" style="height:689px">
    <div class="ghost">JOBANGEBOTE</div>
    <span class="bar"></span>
    <h2 class="sec-title"><span class="red">Über</span> uns</h2>
    <h4 class="team-line">Tolles, erfolgreiches und kreatives Team mit insgesamt 15 Kollegen/innen</h4>
    <ul class="perks">
      <li><svg width="16" height="10" viewBox="0 0 16 10" fill="none" stroke="#1e264a" stroke-width="1.3"><path d="M0 5h15M11 1l4 4-4 4"/></svg>Spaß an der Arbeit</li>
      <li><svg width="16" height="10" viewBox="0 0 16 10" fill="none" stroke="#1e264a" stroke-width="1.3"><path d="M0 5h15M11 1l4 4-4 4"/></svg>Entwicklung von Softwarelösungen für alle Teilnehmer im Gesundheitsmarkt</li>
      <li><svg width="16" height="10" viewBox="0 0 16 10" fill="none" stroke="#1e264a" stroke-width="1.3"><path d="M0 5h15M11 1l4 4-4 4"/></svg>Cooles Büro- Beste Arbeitsmittel</li>
      <li><svg width="16" height="10" viewBox="0 0 16 10" fill="none" stroke="#1e264a" stroke-width="1.3"><path d="M0 5h15M11 1l4 4-4 4"/></svg>Wir wachsen und suchen Verstärkung</li>
    </ul>

    <div class="job-card">
      <span class="tag">Öffnungen</span>
      <svg style="margin-top:26px" width="60" height="70" viewBox="0 0 60 70" fill="none" stroke="#e30713" stroke-width="2"><rect x="32" y="4" width="24" height="18" rx="3"/><path d="M40 10l-3 3 3 3M48 10l3 3-3 3"/><circle cx="24" cy="26" r="11"/><path d="M4 66c0-14 9-22 20-22s20 8 20 22z"/></svg>
      <p class="role">Full Stack Entwickler (m/w/d)</p>
      <p class="desc">Festanstellung, Vollzeit in Musterstadt<br>/ VMT Pflegelösung AG</p>
    </div>

    <h4 class="question">Genug von uns, jetzt zu dir. Kannst du nachfolgende Skills größtenteils mit JA beantworten?</h4>

    <div class="skills">
      <div class="skill" style="left:0">
        <h4>Bereiche:</h4>
        <ul><li>C#, .Net / .Net Core und/oder</li><li>Java, Spring, SpringBoot und/oder</li><li>Angular, Typescript, Javascript</li></ul>
      </div>
      <div class="skill" style="left:264px">
        <h4>Technische Skills:</h4>
        <ul><li class="plain">gute Kenntnisse in:</li><li>SQL</li><li>RESTful APIs</li><li>Git oder TFS</li><li>Docker</li></ul>
      </div>
      <div class="skill" style="left:460px">
        <h4>Wünschenswert:</h4>
        <ul><li>App-Entwicklung mit IONIC</li><li>Powerbuilder</li><li>Confluence und Jira</li><li>Bitbucket</li><li>Jenkins</li></ul>
      </div>
      <div class="skill" style="left:693px;width:210px">
        <h4>Fachliche Skills:</h4>
        <ul><li>Bereitschaft sich in neue Technologien einzuarbeiten</li><li>Agile Softwareentwicklung (Kanban / Scrum)</li><li>wünschenswert: Kenntnisse im Gesundheitswesen (insb. Apothekenmarkt)</li></ul>
      </div>
    </div>

    <div class="apply">
      <div class="apply-left">Cool. Dann bewirb dich schnell mit Gehaltsvorstellung per Mail bei uns. Wir haben einiges zu bieten.</div>
      <div class="apply-right">
        <p class="lbl">Ansprechpartner:</p>
        <div class="contact">
          <svg width="28" height="28" viewBox="0 0 28 28" fill="none" stroke="#fff" stroke-width="1.5"><circle cx="14" cy="14" r="13"/><circle cx="14" cy="11" r="4.5"/><path d="M6 23c2-5 14-5 16 0"/></svg>
          <div><b>Tobias Kwenrich</b><br>kwenrich@vmt-pflegeloesung.de</div>
        </div>
      </div>
    </div>
  </div>
</section>

<section class="quotes">
  <div class="red-half"></div>
  <div class="qmark">“</div>
  <div class="quote" style="left:152px">
    <svg class="avatar" viewBox="0 0 50 50" fill="none" stroke="#fff" stroke-width="2" role="img" aria-label="Platzhalter Kundenfoto"><circle cx="25" cy="20" r="8"/><path d="M11 41c3-9 25-9 28 0"/></svg>
    <p class="text">Duis aute irure dolor in reprehenderit in voluptate velit esse cillum dolore eu fugiat nulla pariatur. Excepteur sint occaecat cupidatat non proident, sunt in culpa qui officia deserunt mollit anim id est laborum.</p>
    <p class="who">- Mara Olsen</p>
  </div>
  <div class="quote" style="left:678px">
    <svg class="avatar" viewBox="0 0 50 50" fill="none" stroke="#fff" stroke-width="2" role="img" aria-label="Platzhalter Kundenfoto"><circle cx="25" cy="20" r="8"/><path d="M11 41c3-9 25-9 28 0"/></svg>
    <p class="text">Duis aute irure dolor in reprehenderit in voluptate velit esse cillum dolore eu fugiat nulla pariatur. Excepteur sint occaecat cupidatat non proident, sunt in culpa qui officia deserunt mollit anim id est laborum.</p>
    <p class="who">- Mara Olsen</p>
  </div>
</section>

<footer class="site-footer">
  <div class="wrap" style="height:96px">
    <a class="brand" href="#"><span class="brand-dot"></span>VMT</a>
    <div class="f-item" style="left:200px;top:26px;font-weight:700">
      <svg width="14" height="16" viewBox="0 0 14 16"><path d="M7 0a6 6 0 0 1 6 6c0 4-6 10-6 10S1 10 1 6a6 6 0 0 1 6-6z" fill="#e30713"/><circle cx="7" cy="6" r="2" fill="#fff"/></svg>
      VMT AG, Lindenweg 12, 40210 Musterstadt
    </div>
    <div class="f-item" style="left:200px;top:52px">
      <svg width="14" height="14" viewBox="0 0 24 24" fill="none" stroke="#e30713" stroke-width="2"><path d="M5 3h4l2 5-2.5 1.5a11 11 0 0 0 6 6L16 13l5 2v4a2 2 0 0 1-2 2A17 17 0 0 1 3 5a2 2 0 0 1 2-2z"/></svg>
      +49 30 55 / 1 20 48 -00
    </div>
    <div class="f-item" style="left:460px;top:26px">
      <svg width="14" height="14" viewBox="0 0 16 16" fill="none" stroke="#e30713" stroke-width="1.3"><path d="M1 7l14-6-5 14-3-5z"/></svg>
      info@vmt-pflegeloesung.de
    </div>
    <div class="f-item" style="left:460px;top:48px">
      <svg width="14" height="14" viewBox="0 0 16 16" fill="none" stroke="#e30713" stroke-width="1.3"><circle cx="8" cy="8" r="7"/><path d="M1 8h14M8 1c-3 3-3 11 0 14M8 1c3 3 3 11 0 14"/></svg>
      vmt-pflegeloesung.de
    </div>
    <div class="legal">DATENSCHUTZ | IMPRESSUM</div>
  </div>
</footer>

</body>
</html>
```